Business Card for Bloom Vitality & Strength

Hi can you please design a business card with my logo and program logo (the new one I just sent) somewhere on it too maybe on the back? Needs to be eye catching and super cool.
Trudy Melcombe, Director
Master Personal Trainer & Nutrition Coach
0472 816 305
Www.bloomvitalitystrength.com.au
Insta (logo) bloom_vitality_strength #bloomyou7x72018

Target Market(s)

30+ women looking to change lifestyle to healthy mind body etc

Industry/Entity Type

Health And Wellness

Contact Information for Business Card

As above

Font styles to use
Sans Serif

Colors

Designer to choose colors to be used in the design.

Requirements
Must have
• Must super cool and edgy with a bit of cuteness

```html
<!DOCTYPE html>
<html lang="en">
<head>
<meta charset="utf-8">
<title>Bloom Vitality &amp; Strength — Business Card</title>
<link rel="stylesheet" href="https://fonts.googleapis.com/css2?family=Fjalla+One&family=Roboto:wght@400;700&display=swap">
<style>
  :root {
    --page-bg: #e4e1de;
    --card-bg: #f4f2f0;
    --card-edge: #d9d5d1;
    --ink: #1d1d1d;
    --ink-soft: #2b2b2b;
    --accent-red: #9b1a1c;
    --rule: #6a6a6a;
  }
  * { margin: 0; padding: 0; box-sizing: border-box; }
  html, body {
    width: 1200px; height: 1054px; overflow: hidden;
    background: var(--page-bg);
  }
  .card {
    position: absolute; left: 100px; top: 227px;
    width: 1000px; height: 600px;
    background: var(--card-bg);
    border: 1px solid var(--card-edge);
    border-radius: 6px;
    box-shadow: 0 10px 30px rgba(0,0,0,0.12);
    font-family: "Roboto", sans-serif;
    color: var(--ink);
  }
  .holder { position: absolute; left: 50px; top: 100px; }
  .holder-name {
    font-family: "Fjalla One", sans-serif;
    font-size: 39px; line-height: 1.1;
    color: var(--accent-red);
  }
  .holder-role {
    margin-top: 16px;
    font-size: 23px; line-height: 1.36;
    color: var(--ink-soft);
  }
  .brand {
    position: absolute; right: 48px; top: 110px;
    display: flex; align-items: center; gap: 16px;
  }
  .brand-dot {
    width: 54px; height: 54px; border-radius: 50%;
    background: var(--accent-red);
  }
  .brand-name {
    font-weight: 700; font-size: 34px; line-height: 1.15;
    color: var(--ink); text-transform: uppercase;
    letter-spacing: 0.5px;
  }
  .contacts {
    position: absolute; left: 50px; top: 412px;
    list-style: none;
  }
  .contacts li {
    display: flex; align-items: center; gap: 26px;
    height: 37px; font-size: 23px; color: var(--ink-soft);
  }
  .contacts svg { width: 22px; height: 22px; fill: var(--accent-red); flex: none; }
  .program {
    position: absolute; left: 748px; top: 470px; width: 205px;
    text-align: center;
  }
  .program-rule { height: 1px; background: var(--rule); }
  .program-name {
    font-size: 26px; letter-spacing: 2px; padding: 6px 0 4px;
    color: var(--ink);
  }
  .program-by {
    font-size: 12px; color: var(--ink-soft); margin-top: 5px;
    text-align: right;
  }
</style>
</head>
<body>
  <main class="card">
    <section class="holder">
      <h1 class="holder-name">Trudy Melcombe, Director</h1>
      <p class="holder-role">Master Personal Trainer<br>&amp; Nutrition Coach</p>
    </section>

    <div class="brand">
      <span class="brand-dot"></span>
      <span class="brand-name">Bloom Vitality<br>&amp; Strength</span>
    </div>

    <ul class="contacts">
      <li>
        <svg viewBox="0 0 24 24" aria-hidden="true"><path d="M3 8c0-2 4-4 9-4s9 2 9 4v2h-5V8c-1-.6-2.5-1-4-1s-3 .4-4 1v2H3zM6 11h12l2 8H4zM12 13a2.5 2.5 0 1 0 0 5 2.5 2.5 0 0 0 0-5z"/></svg>
        0472 816 305
      </li>
      <li>
        <svg viewBox="0 0 24 24" aria-hidden="true"><path d="M2 5h20v14H2zM4 7v.5l8 5.5 8-5.5V7zM4 10v7h16v-7l-8 5.5z"/></svg>
        trudy@bloomvitalitystrength.com.au
      </li>
      <li>
        <svg viewBox="0 0 24 24" aria-hidden="true"><path d="M12 2a10 10 0 1 0 0 20 10 10 0 0 0 0-20zm0 2c.9 0 2.2 2 2.7 5H9.3C9.8 6 11.1 4 12 4zM9 11h6a17 17 0 0 1 0 2H9a17 17 0 0 1 0-2zm-5 0h3a19 19 0 0 0 0 2H4a8 8 0 0 1 0-2zm13 0h3a8 8 0 0 1 0 2h-3a19 19 0 0 0 0-2zM9.3 15h5.4c-.5 3-1.8 5-2.7 5s-2.2-2-2.7-5z"/></svg>
        www.bloomvitalitystrength.com.au
      </li>
      <li>
        <svg viewBox="0 0 24 24" aria-hidden="true"><path d="M3 3h18v18H3zM5 5v14h14V5z"/></svg>
        #bloom_vitality_strength, #bloomyou7x72018
      </li>
    </ul>

    <div class="program">
      <div class="program-rule"></div>
      <div class="program-name">BloomYou7x7</div>
      <div class="program-rule"></div>
      <div class="program-by">By Bloom Vitality &amp; Strength</div>
    </div>
  </main>
</body>
</html>
```